Digital Agency Needs a Relaunch

We are looking for a modern, top-notch design to elevate our brand to win new clients. It has to build on the clarity of message in the current wireframes and must fit together well on Wordpress.

The winning designer will need to complete the other pages, but please focus on the homepage as the base of your proposed designs for us.

Use the existing logo as a point, and the colour scheme should be around that, we currently use these colours, but you can suggest new mixes:
Purple: #5c306b
Orange: #e27927
Grey: #5f4f61
Light grey: #cacaca
Off white: #ececec
Blue: #674ea7
Updates

Need extra days to review

Target Market(s)

Decent Sized SME Businesses (20+ Staff, Over £1m turnover)

Industry/Entity Type

Digital Marketing

Number of Pages Required

5+ page

Font styles to use
Sans Serif

Colors

Designer to choose colors to be used in the design.

Requirements
Must have
• A real attention on the design piece. Ignore the current website and really focus on the messaging and the brief.
Nice to have
• Read the messages and think about the impact. Use the purple in the logo more than the orange, but try to keep it smart rather than cool
Should not have
• Inconsistent design, serif fonts, stock images and not meeting the wireframes.

```html
<!DOCTYPE html>
<html lang="en">
<head>
<meta charset="utf-8">
<title>Vanta Digital – Growth Works For You</title>
<link href="https://fonts.googleapis.com/css2?family=Raleway:wght@400;500;600;700;800;900&display=swap" rel="stylesheet">
<style>
:root{
  --night:#1c1536;
  --night-2:#2a1b47;
  --night-3:#3d2160;
  --purple:#5c306b;
  --orange:#e96b25;
  --orange-soft:#f08a3c;
  --grey:#5f4f61;
  --light-grey:#cacaca;
  --off-white:#ececec;
  --paper:#f6f6f6;
  --white:#ffffff;
  --text:#4a4550;
}
*{box-sizing:border-box;margin:0;padding:0}
html,body{width:1200px;height:4259px;overflow:hidden}
body{position:relative;font-family:'Raleway',sans-serif;color:var(--text);background:var(--white)}
.abs{position:absolute}
a{color:inherit;text-decoration:none}

/* backgrounds */
.hero-bg{left:0;top:0;width:1200px;height:1100px;background:radial-gradient(ellipse at 80% 60%,#4a2566 0%,var(--night-2) 45%,var(--night) 100%)}
.services-bg{left:0;top:1080px;width:1200px;height:880px;background:linear-gradient(180deg,var(--night) 0%,#241a44 60%,var(--night-2) 100%)}
.footer-bg{left:0;top:3700px;width:1200px;height:559px;background:linear-gradient(180deg,#23193f 0%,var(--night) 100%)}
.shape{left:0;width:1200px}

/* top bar + header */
.topbar{right:210px;top:0;height:26px;padding:0 22px;background:rgba(255,255,255,.06);border-radius:0 0 0 18px;display:flex;gap:10px;align-items:center;font-size:10px;color:var(--orange)}
.topbar span.sep{color:var(--orange)}
.brand{left:207px;top:34px;display:flex;align-items:center;gap:10px;color:var(--white);font-size:34px;font-weight:500;letter-spacing:1px}
.brand-dot{width:16px;height:16px;border-radius:50%;background:var(--white)}
.brand small{position:absolute;left:40px;top:40px;font-size:12px;letter-spacing:7px;font-weight:500}
.nav{left:578px;top:56px;display:flex;gap:25px;color:var(--white);font-size:13px;font-weight:600}

/* hero */
.hero-title{left:0;top:158px;width:1200px;text-align:center;font-weight:900;font-size:50px;line-height:50px;color:var(--white);letter-spacing:1px}
.hero-title .accent{color:var(--orange);display:block}
.cloud{background:var(--white);border-radius:40px}
.rocket-art{left:530px;top:270px;width:140px;height:270px;border-radius:70px 70px 30px 30px;background:linear-gradient(180deg,#ffffff 0%,#f0eef4 55%,var(--orange) 100%)}
.scroll-hint{left:591px;top:540px;width:18px;height:40px}

/* intro */
.intro-head{left:0;top:674px;width:1200px;text-align:center;color:var(--purple);font-weight:800;font-size:24px;line-height:38px}
.intro-copy{left:395px;top:765px;width:410px;text-align:center;font-size:12.5px;line-height:23px;color:var(--text)}
.intro-copy p{margin-bottom:21px}
.intro-cta{left:0;top:1011px;width:1200px;text-align:center;color:var(--purple);font-weight:800;font-size:17px}
.btn{display:flex;align-items:center;justify-content:center;gap:8px;border-radius:22px;font-size:12.5px}
.btn-solid{background:var(--orange);color:var(--white)}
.btn-line{border:1.5px solid var(--orange);color:var(--orange);background:var(--white)}

/* services */
.service{width:218px;height:236px;border:1.5px solid var(--orange);border-radius:26px;background:rgba(28,21,54,.6);padding:26px 0 0 20px}
.service h3{color:var(--orange);font-weight:800;font-size:17px;text-align:center;margin-left:-20px;margin-bottom:14px;letter-spacing:.5px}
.service ul{list-style:none}
.service li{display:flex;align-items:center;gap:8px;color:var(--white);font-weight:800;font-size:11.5px;height:34px}
.service svg{width:24px;height:24px;flex:none}

/* pain / gain */
.pg-line{height:1.5px;background:var(--orange)}
.pg-circle{border-radius:50%;box-shadow:0 6px 14px rgba(0,0,0,.25)}
.pg-label{font-weight:800;font-size:14px}
.pg-text{font-size:11.5px;font-style:italic;line-height:18px;color:var(--grey)}

/* about */
.about-head{left:207px;top:2226px;display:flex;align-items:center;gap:8px;font-size:19px;font-weight:600;color:var(--purple)}
.about-head .accent{color:var(--orange)}
.about-mark{width:20px;height:20px;border:2px solid var(--orange);border-radius:50%}
.about-copy{left:207px;top:2264px;width:310px;font-size:12px;line-height:19px;color:var(--text)}
.about-copy p{margin-bottom:18px}
.about-copy .link{color:var(--orange);text-decoration:underline}
.about-photo{left:547px;top:2173px;width:480px;height:480px;border-radius:50%;background:radial-gradient(circle at 50% 45%,#e8e8ea 0%,#8a8a92 30%,#1d1d24 62%,#0c0c10 100%);box-shadow:0 10px 24px rgba(0,0,0,.25)}

/* case studies */
.cases-bg{left:0;top:2711px;width:1200px;height:377px;background:var(--off-white)}
.section-title{font-weight:900;font-size:24px;color:var(--purple);letter-spacing:.5px}
.case{top:2800px;width:187px;height:218px;border-radius:6px;overflow:hidden}
.case .logo{position:absolute;left:0;top:72px;width:100%;text-align:center;font-weight:800;font-size:26px;color:var(--night)}
.case .more{position:absolute;left:0;top:168px;width:155px;height:28px;border-radius:0 14px 14px 0;background:var(--orange);color:var(--white);font-weight:700;font-style:italic;font-size:12px;display:flex;align-items:center;justify-content:center}
.arrow{width:34px;height:34px;border-radius:50%;display:flex;align-items:center;justify-content:center}

/* blog */
.post{top:3273px;width:238px;height:248px;background:var(--paper);box-shadow:0 4px 12px rgba(0,0,0,.14)}
.post .thumb{height:150px;position:relative}
.post .tag{position:absolute;left:0;bottom:0;width:95px;height:26px;background:var(--night-3);border-radius:0 13px 13px 0;color:var(--white);font-size:10.5px;font-weight:700;padding:6px 0 0 16px}
.post h4{margin:27px 18px 0;font-size:11px;font-weight:500;line-height:16px;color:var(--grey);text-transform:uppercase}
.post .read{margin:10px 18px 0;font-size:9.5px;font-weight:800;color:var(--orange)}

/* cta bar */
.cta-bar{left:288px;top:3690px;width:624px;height:66px;border:1.5px solid var(--purple);border-radius:33px;background:var(--white);display:flex;align-items:center;padding-left:22px;gap:10px;font-size:12.5px;color:var(--grey)}
.cta-bar .btn{position:absolute;right:9px;top:13px;width:181px;height:40px}

/* footer */
.f-col h5{font-weight:500;font-size:15px;color:var(--orange);margin-bottom:10px}
.f-col ul{list-style:none}
.f-col li{color:var(--white);font-weight:600;font-size:12.5px;line-height:22px}
.f-col li::before{content:"• "}
.f-address{color:var(--white);font-weight:600;font-size:12.5px;line-height:22px}
.f-rocket{border-radius:50%;background:radial-gradient(circle,rgba(255,255,255,.14) 0%,rgba(233,107,37,.12) 45%,rgba(28,21,54,0) 70%)}
.legal{font-size:10px;color:var(--white)}
</style>
</head>
<body>

<!-- HERO -->
<div class="abs hero-bg"></div>
<div class="abs topbar"><a>Blog</a><span class="sep">|</span><a>About Us</a><span class="sep">|</span><a>Contact Us</a><span class="sep">|</span><a>01 555 010 200</a></div>
<div class="abs brand"><span class="brand-dot"></span>vanta<small>DIGITAL</small></div>
<nav class="abs nav"><a>Create</a><a>Communicate</a><a>Convert</a><a>Close</a><a>Case Studies</a></nav>
<h1 class="abs hero-title">GROWTH WORKS<span class="accent">FOR YOU</span></h1>

<div class="abs cloud" role="img" aria-label="Cloud" style="left:193px;top:305px;width:160px;height:90px;border-radius:50px 60px 24px 24px"></div>
<div class="abs cloud" role="img" aria-label="Cloud" style="left:253px;top:450px;width:78px;height:42px;border-radius:24px 28px 14px 14px"></div>
<div class="abs cloud" role="img" aria-label="Cloud" style="left:728px;top:265px;width:115px;height:50px;border-radius:30px 30px 14px 14px"></div>
<div class="abs cloud" role="img" aria-label="Cloud" style="left:875px;top:423px;width:135px;height:75px;border-radius:40px 50px 20px 20px"></div>
<div class="abs rocket-art" role="img" aria-label="Illustrated rocket lifting off on a cloud of smoke"></div>
<svg class="abs scroll-hint" viewBox="0 0 18 40" aria-hidden="true"><circle cx="9" cy="6" r="5" fill="none" stroke="#5c306b" stroke-width="1.5"/><path d="M9 14v22M3 30l6 6 6-6" fill="none" stroke="#5c306b" stroke-width="1.5"/></svg>

<!-- white intro shape -->
<svg class="abs shape" style="top:560px" width="1200" height="620" viewBox="0 0 1200 620" aria-hidden="true">
  <path d="M0 120 Q600 -45 1200 120 L1200 535 Q600 680 0 535 Z" fill="#f6f6f6"/>
</svg>

<h2 class="abs intro-head">Fed up with agencies who don’t care?<br>We’ve heard that before</h2>
<div class="abs intro-copy">
  <p>We know every client has unique needs. Yet, few digital agencies spend enough time getting to know the client’s business.</p>
  <p>We’re different. We take a highly personalised approach to every project, working closely with our clients to understand their objectives, challenges, and target audience.</p>
  <p>Knowing your business is the first step in helping you grow. It’s how we work, and it will work for you.</p>
</div>
<div class="abs intro-cta">ACHIEVE GROWTH THAT WORKS</div>
<a class="abs btn btn-solid" style="left:516px;top:1053px;width:168px;height:40px">Set Up A Call
  <svg width="16" height="16" viewBox="0 0 16 16" aria-hidden="true"><path d="M3 13l3-1 6-6a3 3 0 0 0-2-2L4 10z M10 4l2-2" fill="none" stroke="#fff" stroke-width="1.3"/></svg></a>

<!-- SERVICES -->
<div class="abs services-bg" style="z-index:-1"></div>
<svg class="abs shape" style="top:1080px;z-index:-1" width="1200" height="100" aria-hidden="true"><rect width="1200" height="100" fill="#1c1536"/></svg>

<section class="abs service" style="left:337px;top:1278px">
  <h3>CREATE</h3>
  <ul>
    <li><svg viewBox="0 0 24 24"><circle cx="12" cy="12" r="5" fill="none" stroke="#fff" stroke-width="1.3"/><path d="M12 2v4M12 18v4M2 12h4M18 12h4M5 5l3 3M16 16l3 3M5 19l3-3M16 8l3-3" stroke="#fff" stroke-width="1.3"/></svg>• BRANDING</li>
    <li><svg viewBox="0 0 24 24"><rect x="4" y="8" width="14" height="12" fill="none" stroke="#fff" stroke-width="1.3"/><path d="M10 16l10-12" stroke="#fff" stroke-width="1.3"/></svg>• GRAPHICS</li>
    <li><svg viewBox="0 0 24 24"><rect x="3" y="6" width="18" height="14" fill="none" stroke="#fff" stroke-width="1.3"/><path d="M10 10v6l5-3z" fill="none" stroke="#fff" stroke-width="1.3"/></svg>• VIDEO</li>
    <li><svg viewBox="0 0 24 24"><rect x="5" y="3" width="12" height="18" rx="2" fill="none" stroke="#fff" stroke-width="1.3"/><path d="M19 7v10" stroke="#fff" stroke-width="1.3"/></svg>• CONTENT</li>
  </ul>
</section>
<section class="abs service" style="left:643px;top:1278px">
  <h3>COMMUNICATE</h3>
  <ul>
    <li><svg viewBox="0 0 24 24"><path d="M3 10h4l10-5v14L7 14H3z M7 14l2 6" fill="none" stroke="#fff" stroke-width="1.3"/></svg>• ADS</li>
    <li><svg viewBox="0 0 24 24"><circle cx="6" cy="7" r="2" fill="none" stroke="#fff"/><circle cx="12" cy="7" r="2" fill="none" stroke="#fff"/><circle cx="18" cy="7" r="2" fill="none" stroke="#fff"/><circle cx="9" cy="16" r="2" fill="none" stroke="#fff"/><circle cx="15" cy="16" r="2" fill="none" stroke="#fff"/></svg>• ORGANIC</li>
    <li><svg viewBox="0 0 24 24"><path d="M12 20a8 7 0 1 0-6-3l-2 4 5-2" fill="none" stroke="#fff" stroke-width="1.3"/><path d="M12 14l-3-3a2 2 0 0 1 3-2 2 2 0 0 1 3 2z" fill="none" stroke="#fff"/></svg>• SOCIAL</li>
    <li><svg viewBox="0 0 24 24"><rect x="2" y="5" width="20" height="14" fill="none" stroke="#fff" stroke-width="1.3"/><path d="M2 5l10 8 10-8" fill="none" stroke="#fff" stroke-width="1.3"/></svg>• EMAIL</li>
  </ul>
</section>
<section class="abs service" style="left:337px;top:1549px">
  <h3>CONVERT</h3>
  <ul>
    <li><svg viewBox="0 0 24 24"><rect x="3" y="5" width="18" height="14" fill="none" stroke="#fff" stroke-width="1.3"/><path d="M3 9h18M9 13h6" stroke="#fff" stroke-width="1.3"/></svg>• WEBSITES</li>
    <li><svg viewBox="0 0 24 24"><circle cx="12" cy="12" r="8" fill="none" stroke="#fff" stroke-width="1.3" stroke-dasharray="3 2"/><circle cx="12" cy="12" r="3" fill="none" stroke="#fff"/></svg>• LEAD GENERATION</li>
    <li><svg viewBox="0 0 24 24"><rect x="3" y="4" width="18" height="14" fill="none" stroke="#fff" stroke-width="1.3"/><path d="M8 9h8l-1 4H9z M9 21h6" fill="none" stroke="#fff"/></svg>• E-COMMERCE</li>
    <li><svg viewBox="0 0 24 24"><circle cx="11" cy="11" r="7" fill="none" stroke="#fff" stroke-width="1.3"/><path d="M16 16l5 5M8 11l2 2 4-4" fill="none" stroke="#fff" stroke-width="1.3"/></svg>• ANALYTICS</li>
  </ul>
</section>
<section class="abs service" style="left:643px;top:1549px">
  <h3>CLOSE</h3>
  <ul>
    <li><svg viewBox="0 0 24 24"><circle cx="12" cy="12" r="8" fill="none" stroke="#fff" stroke-width="1.3"/><circle cx="12" cy="10" r="3" fill="none" stroke="#fff"/><path d="M7 18a5 4 0 0 1 10 0" fill="none" stroke="#fff"/></svg>• CRM</li>
    <li><svg viewBox="0 0 24 24"><circle cx="12" cy="12" r="4" fill="none" stroke="#fff" stroke-width="1.3"/><path d="M12 2v5M12 17v5M2 12h5M17 12h5" stroke="#fff" stroke-width="2"/></svg>• SYSTEMS</li>
    <li><svg viewBox="0 0 24 24"><circle cx="12" cy="7" r="3" fill="none" stroke="#fff" stroke-width="1.3"/><path d="M6 21v-5a6 6 0 0 1 12 0v5z" fill="none" stroke="#fff" stroke-width="1.3"/></svg>• CUSTOMER SUCCESS</li>
    <li><svg viewBox="0 0 24 24"><rect x="7" y="6" width="10" height="9" rx="2" fill="none" stroke="#fff" stroke-width="1.3"/><path d="M12 2v4M9 15v6M15 15v6M4 10h3M17 10h3" stroke="#fff" stroke-width="1.3"/></svg>• AI &amp; AUTOMATIONS</li>
  </ul>
</section>

<!-- white lower shape -->
<svg class="abs shape" style="top:1845px" width="1200" height="1900" viewBox="0 0 1200 1900" aria-hidden="true">
  <path d="M0 90 Q600 -50 1200 90 L1200 1886 Q600 1950 0 1886 Z" fill="#ffffff"/>
</svg>

<!-- PAIN / GAIN -->
<div class="abs pg-line" style="left:300px;top:1934px;width:600px"></div>
<div class="abs pg-line" style="left:300px;top:2060px;width:600px"></div>
<div class="abs pg-circle" role="img" aria-label="Broken rocket crashed in a cloud of smoke" style="left:182px;top:1911px;width:172px;height:172px;background:radial-gradient(circle at 50% 60%,#8e8e8e 0%,#4a4a4a 55%,#333 100%)"></div>
<div class="abs pg-circle" role="img" aria-label="Rocket flying upward with an orange trail" style="left:843px;top:1911px;width:172px;height:172px;background:radial-gradient(circle at 50% 50%,#3d2160 0%,#26183f 70%)"></div>
<div class="abs pg-label" style="left:367px;top:1952px;color:var(--night)">YOUR PAIN?</div>
<div class="abs pg-text" style="left:364px;top:1978px;width:210px">“I spend most of my development budget fixing errors and bugs”</div>
<svg class="abs" style="left:582px;top:1979px" width="36" height="36" viewBox="0 0 36 36" aria-hidden="true"><circle cx="18" cy="18" r="17" fill="#fff" stroke="#e5e5e5"/><path d="M14 11v14l11-7z" fill="none" stroke="#e96b25" stroke-width="2" stroke-linejoin="round"/></svg>
<div class="abs pg-label" style="left:641px;top:1952px;color:var(--orange)">FUTURE GAIN</div>
<div class="abs pg-text" style="left:641px;top:1978px;width:200px">A fast &amp; reliable cash-generative content-managed e-commerce or lead generation website</div>
<div class="abs btn btn-solid" style="left:641px;top:2047px;width:112px;height:26px;font-size:10px">Websites</div>

<!-- ABOUT -->
<div class="abs about-head"><span class="about-mark"></span>VANTA: WHERE <span class="accent">GROWTH</span> WORKS</div>
<div class="abs about-copy">
  <p>We understand the importance of a strong online presence. That’s why we offer a complete range of digital marketing solutions to help you reach your growth goals.</p>
  <p>Our <span class="link">track record</span> demonstrates expertise in all forms of digital marketing, including <span class="link">Website builds</span>, <span class="link">Lookwise Ads</span>, <span class="link">SEO</span>, <span class="link">Email Marketing</span>.</p>
  <p>We’re constantly staying up-to-date on the latest trends, tech and best practices in the industry, so you can trust that you’re getting the most effective and efficient strategies for your business growth.</p>
  <p>Set up a call and we’re confident we can show you where we can add growth and value to your business.</p>
</div>
<div class="abs about-photo" role="img" aria-label="Photo of an astronaut in a white spacesuit holding a laptop against a dark background"></div>

<!-- CASE STUDIES -->
<div class="abs cases-bg"></div>
<h2 class="abs section-title" style="left:205px;top:2742px">CREATE <span style="color:var(--grey);font-size:16px">→</span> CASE STUDIES</h2>
<div class="abs case" role="img" aria-label="Faded photo of a previous project" style="left:0;width:190px;background:linear-gradient(90deg,rgba(236,236,236,1) 0%,#b9cfe0 100%);opacity:.7"></div>
<div class="abs case" style="left:205px;background:linear-gradient(180deg,#8b95a0,#c3c8ce)" role="img" aria-label="Project photo with client name">
  <div class="logo">KESTREL</div><div class="more">LEARN MORE</div></div>
<div class="abs case" style="left:406px;background:linear-gradient(180deg,#c7c9cc,#9ea2a8)" role="img" aria-label="Project dashboard screenshot with client name">
  <div class="logo">ARLO</div><div class="more">LEARN MORE</div></div>
<div class="abs case" style="left:606px;background:linear-gradient(180deg,#a8a19c,#d7d2cd)" role="img" aria-label="Phone showing a sailing website with client name">
  <div class="logo" style="font-size:17px;color:var(--grey)">TIDEWIND<br><span style="font-size:10px;letter-spacing:3px">SAILING</span></div><div class="more">LEARN MORE</div></div>
<div class="abs arrow" style="left:834px;top:2892px;border:1.5px solid var(--light-grey)"><svg width="12" height="12" viewBox="0 0 12 12" aria-hidden="true"><path d="M8 1L3 6l5 5" fill="none" stroke="#cacaca" stroke-width="1.5"/></svg></div>
<div class="abs arrow" style="left:888px;top:2892px;border:1.5px solid var(--orange)"><svg width="12" height="12" viewBox="0 0 12 12" aria-hidden="true"><path d="M4 1l5 5-5 5" fill="none" stroke="#e96b25" stroke-width="1.5"/></svg></div>

<!-- BLOG -->
<h2 class="abs section-title" style="left:0;top:3192px;width:1200px;text-align:center">FROM THE BLOG</h2>
<article class="abs post" style="left:207px">
  <div class="thumb" role="img" aria-label="Photo of a person working at a desk with a laptop" style="background:linear-gradient(135deg,#d9d9dc,#8d8f95)"><span class="tag">Tech</span></div>
  <h4>Lookwise’s new PPC features are loaded with AI</h4><div class="read">READ MORE...</div>
</article>
<article class="abs post" style="left:481px">
  <div class="thumb" role="img" aria-label="Photo of a laptop on a table with cables" style="background:linear-gradient(135deg,#f0f0f0,#7f8186)"><span class="tag">Tech</span></div>
  <h4>How Lookwise killed the broad match keyword?</h4><div class="read">READ MORE...</div>
</article>
<article class="abs post" style="left:755px">
  <div class="thumb" role="img" aria-label="Photo of two colleagues looking at a laptop" style="background:linear-gradient(135deg,#c4c8cf,#545a66)"><span class="tag">Social Media</span></div>
  <h4>The 9 rules of social media engagement</h4><div class="read">READ MORE...</div>
</article>
<a class="abs btn btn-line" style="left:514px;top:3573px;width:172px;height:40px">Visit Blog</a>

<!-- CTA -->
<div class="abs cta-bar">
  <svg width="20" height="20" viewBox="0 0 20 20" aria-hidden="true"><circle cx="10" cy="10" r="8" fill="none" stroke="#e96b25" stroke-width="2"/></svg>
  We’re the turbo boost for your digital marketing engine
  <a class="btn btn-solid">Put Your Foot Down
    <svg width="16" height="16" viewBox="0 0 16 16" aria-hidden="true"><path d="M3 13l3-1 6-6a3 3 0 0 0-2-2L4 10z M10 4l2-2" fill="none" stroke="#fff" stroke-width="1.3"/></svg></a>
</div>

<!-- FOOTER -->
<div class="abs footer-bg" style="z-index:-1"></div>
<div class="abs f-rocket" role="img" aria-label="Faint illustrated rocket" style="left:640px;top:3990px;width:300px;height:300px"></div>
<div class="abs f-rocket" role="img" aria-label="Faint illustrated rocket" style="left:530px;top:4120px;width:140px;height:140px"></div>
<div class="abs f-rocket" role="img" aria-label="Faint illustrated rocket" style="left:1010px;top:4100px;width:150px;height:150px"></div>

<div class="abs f-col" style="left:207px;top:3885px"><h5>CREATE</h5><ul><li>Branding</li><li>Graphics</li><li>Video</li><li>Content</li></ul></div>
<div class="abs f-col" style="left:430px;top:3885px"><h5>CONVERT</h5><ul><li>Websites</li><li>Lead Generation</li><li>E-commerce</li><li>Analytics</li></ul></div>
<div class="abs f-col" style="left:641px;top:3885px"><h5>CONNECT</h5><ul><li>Case Studies</li><li>Blog</li><li>About Us</li></ul></div>
<div class="abs f-col" style="left:855px;top:3885px"><h5>CONTACT</h5><ul><li>Contact Us</li><li>Tel: <span style="text-decoration:underline">01 555 010 200</span></li></ul></div>
<div class="abs f-col" style="left:207px;top:4038px"><h5>COMMUNICATE</h5><ul><li>Ads</li><li>Organic</li><li>Social</li><li>Email</li></ul></div>
<div class="abs f-col" style="left:430px;top:4038px"><h5>CLOSE</h5><ul><li>CRM</li><li>Systems</li><li>Customer Success</li><li>AI &amp; Automations</li></ul></div>
<div class="abs f-col" style="left:855px;top:4030px"><h5>ADDRESS</h5>
  <div class="f-address">Harbour Gate House,<br>Lenbury, Westshire<br>LB4 2QT</div></div>

<div class="abs legal" style="left:207px;top:4222px">Vanta Digital Limited. All Rights Reserved</div>
<div class="abs legal" style="left:786px;top:4222px">Sitemap &nbsp;|&nbsp; Terms of Use &nbsp;|&nbsp; Privacy &nbsp;|&nbsp; Policy</div>

</body>
</html>
```